Hopscotch Nell needs updated Marketing Material!

Moving business to a new location and am looking to update all marketing material, including business cards, postcards, flyers, website. I've attached a copy of my current business card.
Updates

Good Morning!  I just received my new business phone number.  It is 583-402-9176

Hello All Designers!

Thank you for all the submissions I have received so far!  I wanted to give you a bit more background on what Hopscotch Nell is all about:

I started this service when I was downsized out of a sales and marketing position.   A friend asked if I had time to run a few errands for her while she was at work.  "Lightbulb"!  I thought there must be more people that are over worked, over booked and want nothing more to do when they get home than spend time with their families or just relaxing.  And who wants to do all their running around on the weekends??  Hopscotch Nell was born!

I have been extremely fortunate with my business here in California.  However, this summer I will be moving to a small town in Pennsylvania and I will be in uncharted territory.  I hope to have marketing material that will "WOW" all new potential clients.  Letting them know that I offer a unique service that can put time back into their week and free up their weekends for more important things.

If there is anything else I can tell you in order to help you with your design process, please let me know!
Thank you!
Nellie

Target Market(s)

Busy working parents and young professionals with disposable income that would like to spend their down time doing things that they enjoy rather than doing errands.

Industry/Entity Type

Marketing

```html
<!DOCTYPE html>
<html lang="en">
<head>
<meta charset="utf-8">
<title>Hopscotch Nell – Business Card</title>
<link href="https://fonts.googleapis.com/css2?family=Arimo:wght@400;700&display=swap" rel="stylesheet">
<style>
  :root {
    --canvas: #ffffff;
    --frame: #2b2b2b;
    --orange: #fe7120;
    --coral: #fe4256;
    --ink: #1e1e1e;
    --white: #ffffff;
    --badge-fill: #e6e6e6;
  }
  * { margin: 0; padding: 0; box-sizing: border-box; }
  html, body {
    width: 1200px; height: 1000px; overflow: hidden;
    background: var(--canvas);
    font-family: "Arimo", Arial, sans-serif;
  }
  .canvas { position: relative; width: 1200px; height: 1000px; }

  .card {
    position: absolute; top: 335px;
    width: 558px; height: 323px;
    border: 6px solid var(--frame);
    overflow: hidden;
  }
  .card--front { left: 44px; background: linear-gradient(to right, var(--orange) 0 278px, var(--coral) 278px); }
  .card--back  { left: 608px; background: linear-gradient(to right, var(--coral) 0 268px, var(--orange) 268px); }

  /* front */
  .brand { position: absolute; left: 10px; top: 127px; color: var(--ink); }
  .brand__name {
    font-size: 21px; font-weight: 400; letter-spacing: 2.2px; line-height: 23px;
    text-transform: uppercase;
  }
  .brand__tagline {
    margin-top: 5px; color: var(--white);
    font-size: 10px; letter-spacing: 0.6px; line-height: 12px; text-transform: uppercase;
  }
  .emblem {
    position: absolute; left: 176px; top: 44px;
    width: 210px; height: 210px; border-radius: 50%;
    border: 7px solid var(--frame);
    background: var(--badge-fill);
  }
  .slogan {
    position: absolute; left: 390px; top: 134px;
    color: var(--white); font-size: 14px; letter-spacing: 1.1px; line-height: 18px;
  }

  /* back */
  .services { position: absolute; left: 8px; top: 58px; list-style: none; }
  .services__item {
    position: relative; padding-left: 15px;
    color: var(--white); font-size: 17.5px; letter-spacing: 2.2px; line-height: 22px;
    margin-bottom: 12px;
    white-space: nowrap;
  }
  .services__item:nth-child(3),
  .services__item:nth-child(4) { margin-bottom: 14px; }
  .services__item::before {
    content: ""; position: absolute; left: 0; top: 6px;
    width: 11px; height: 11px; border-radius: 50%;
    background: var(--frame); border: 1px solid var(--white);
  }
  .contact {
    position: absolute; left: 272px; top: 91px; width: 280px;
    text-align: center; color: var(--ink);
  }
  .contact__name { font-size: 19px; letter-spacing: 3px; line-height: 24px; }
  .contact__phone { margin-top: 5px; font-size: 14px; font-weight: 700; letter-spacing: 2.4px; }
  .contact__line { margin-top: 12px; font-size: 14px; letter-spacing: 2.6px; white-space: nowrap; }
  .contact__line + .contact__line { margin-top: 13px; }
  .contact__line b { font-weight: 700; }
</style>
</head>
<body>
<div class="canvas">
  <section class="card card--front">
    <div class="brand">
      <p class="brand__name">Hopscotch<br>Nell</p>
      <p class="brand__tagline">Personal concierge and<br>errand service</p>
    </div>
    <div class="emblem" role="img" aria-label="Brand emblem: illustration of a running errand-runner with flowing scarf"></div>
    <p class="slogan">“We hop to it so<br>you don’t have to!”</p>
  </section>

  <section class="card card--back">
    <ul class="services">
      <li class="services__item">Personal Shooping and<br>Errands</li>
      <li class="services__item">Household Management</li>
      <li class="services__item">Corporate Concierge</li>
      <li class="services__item">Project Management</li>
      <li class="services__item">Group Rates for<br>Teachers and Seniors</li>
    </ul>
    <div class="contact">
      <p class="contact__name">NELLIE HARLOW</p>
      <p class="contact__phone">583-402-9176</p>
      <p class="contact__line">nellie@hopscotchnell<b>.biz</b></p>
      <p class="contact__line">www.hopscotchnell<b>.biz</b></p>
    </div>
  </section>
</div>
</body>
</html>
```